Business Card Design

We need a business card design for a Executive search firm based in London & the North East called Kestrelby. We specialise in mid - snr level (£50k - £200k) IT placements. Our company colour is navy blue.

Target Market(s)

CEO, HR Director, Sales Director/VP - (35 - 50), well educated, British, European & American

Industry/Entity Type

Business

Contact Information for Business Card

Kestrelby Staffing Limited, Owen Caskell
Mobile - 0044 7731 482 616
London Office - Kestrelby House, 27 Fernmoor, Wexcombe. HA5 3LQ
Tel: 00 44 20 418 62093
North East Office – Velmora Centre, Ashgrove Way, Tillerby, NE41 2RD
Tel: 00 44 191 6842051
www.kestrelbystaffing-example.com

Also the same details for my Business Partner Ravi Tolani
with his mobile number as 0044 7852 307718

Requirements
Must have
• must have the same logo

the logo needs to be the same but made sharper

```html
<!DOCTYPE html>
<html lang="en">
<head>
<meta charset="utf-8">
<title>Kestrelby Business Card</title>
<link href="https://fonts.googleapis.com/css2?family=Questrial&family=Mulish:wght@800&display=swap" rel="stylesheet">
<style>
  :root {
    --navy: #0b4ea2;
    --light-blue: #8ca8d8;
    --grey-text: #8a8a8a;
    --dark-grey: #666666;
    --paper: #ffffff;
    --backdrop: #3b3b3b;
  }
  html, body {
    margin: 0;
    padding: 0;
    width: 1200px;
    height: 1000px;
    overflow: hidden;
    background: var(--backdrop);
    font-family: "Questrial", sans-serif;
  }
  .canvas { position: relative; width: 1200px; height: 1000px; }
  .card {
    position: absolute;
    background: var(--paper);
    box-shadow: 0 14px 28px rgba(0,0,0,0.55);
  }
  .card svg { position: absolute; left: 0; top: 0; }
  .card-front { left: 152px; top: 146px; width: 448px; height: 296px; }
  .card-back  { left: 619px; top: 497px; width: 448px; height: 297px; }

  .wordmark {
    position: absolute;
    left: 228px;
    top: 110px;
    font-size: 20px;
    color: var(--navy);
    display: flex;
    align-items: center;
    gap: 8px;
  }
  .wordmark-dot {
    width: 10px; height: 10px; border-radius: 50%;
    background: var(--navy);
  }

  .back-text { position: absolute; left: 0; right: 0; text-align: center; line-height: 1; }
  .company-name {
    top: 67px;
    font-family: "Mulish", sans-serif;
    font-weight: 800;
    font-size: 21px;
    color: var(--grey-text);
  }
  .person-name {
    top: 110px;
    font-size: 26px;
    color: var(--navy);
  }
  .mobile {
    top: 138px;
    font-size: 10px;
    color: #b0b0b0;
  }
  .office {
    position: absolute;
    top: 176px;
    font-size: 8px;
    line-height: 10px;
    color: #333;
    font-style: normal;
  }
  .office-left { left: 43px; text-align: left; }
  .office-right { right: 43px; text-align: right; }
  .office-title {
    font-size: 14px;
    line-height: 18px;
    color: var(--dark-grey);
    margin-bottom: 4px;
  }
  .website {
    top: 254px;
    font-size: 10px;
    color: var(--navy);
  }
</style>
</head>
<body>
<main class="canvas">

  <section class="card card-front" aria-label="Card front">
    <svg width="448" height="296" viewBox="0 0 448 296">
      <polygon points="8,12 66,12 8,46" fill="var(--navy)"/>
      <polygon points="364,12 440,12 440,70" fill="var(--navy)"/>
      <polygon points="8,160 8,290 186,290" fill="var(--navy)"/>
      <circle cx="67" cy="237" r="11" fill="var(--paper)"/>
      <polygon points="440,234 440,290 412,290" fill="var(--navy)"/>
    </svg>
    <div class="wordmark"><span>kestrelby</span><span class="wordmark-dot"></span></div>
  </section>

  <section class="card card-back" aria-label="Card back">
    <svg width="448" height="297" viewBox="0 0 448 297">
      <polygon points="8,11 439,11 439,55 225,48 8,55" fill="var(--light-blue)"/>
      <polygon points="8,11 439,11 225,48" fill="var(--navy)"/>
      <circle cx="225" cy="30" r="10" fill="var(--paper)"/>
      <circle cx="227" cy="99" r="9" fill="var(--dark-grey)"/>
    </svg>
    <div class="back-text company-name">Kestrelby Staffing Limited</div>
    <div class="back-text person-name">Owen Caskell</div>
    <div class="back-text mobile">Mobile - 0044 7731 482 616</div>

    <address class="office office-left">
      <div class="office-title">London Office</div>
      Kestrelby House<br>
      27 Fernmoor<br>
      Wexcombe. HA5 3LQ<br>
      Tel: 00 44 20 418 62093
    </address>
    <address class="office office-right">
      <div class="office-title">North East Office</div>
      Velmora Centre<br>
      Ashgrove Way<br>
      Tillerby, NE41 2RD<br>
      Tel: 00 44 191 6842051
    </address>

    <div class="back-text website">www.kestrelbystaffing-example.com</div>
  </section>

</main>
</body>
</html>
```